Financial Advisor needs a NEW business card design

We need a new card design as our current design has no white space and clients tend to want to write on the card. I am attaching our current logos and current card design. I have also played with some designs I liked online but don't have the knowledge (or software) to complete the designs in a format that is appropriate for production. I've attached those designs that I liked too. With two office locations and a disclaimer there is a lot of info but we want it to look tidy. We like the deep, rich blue colors and want it to look clean, strong, and modern yet classic.
Business
Included in the attached files

```html
<!DOCTYPE html>
<html lang="en">
<head>
<meta charset="utf-8">
<title>Hartwell Financial Advisory – Business Card</title>
<link href="https://fonts.googleapis.com/css2?family=Lato:wght@400;700&family=Cormorant+Garamond:wght@500&display=swap" rel="stylesheet">
<style>
  :root {
    --navy: #13317a;
    --navy-deep: #0f2a6b;
    --paper: #f7f7f7;
    --ink: #2a2a2a;
    --rule: #9a9a9a;
    --stage: #2b2b2b;
    --white: #ffffff;
  }
  * { box-sizing: border-box; margin: 0; padding: 0; }
  html, body { width: 1200px; height: 900px; overflow: hidden; }
  body {
    background: var(--stage);
    display: flex;
    flex-direction: column;
    align-items: center;
    justify-content: center;
    gap: 40px;
    font-family: "Lato", sans-serif;
  }
  .card {
    position: relative;
    width: 680px;
    height: 389px;
    box-shadow: 0 8px 24px rgba(0,0,0,.45);
  }

  /* Front */
  .card-front {
    background: radial-gradient(ellipse at 50% 40%, var(--navy) 0%, var(--navy-deep) 100%);
    color: var(--white);
  }
  .front-brand {
    position: absolute;
    left: 130px;
    top: 115px;
    width: 420px;
  }
  .brand-name {
    font-family: "Lato", sans-serif;
    font-weight: 400;
    font-size: 30px;
    letter-spacing: 2px;
    line-height: 1.15;
    text-transform: uppercase;
  }
  .brand-name .brand-sub { display: block; font-size: 20px; letter-spacing: 3px; }
  .brand-rule {
    height: 2px;
    margin-top: 10px;
    background: currentColor;
  }
  .disclaimer {
    position: absolute;
    left: 0; right: 0;
    top: 262px;
    text-align: center;
    font-family: "Cormorant Garamond", serif;
    font-weight: 500;
    font-variant: small-caps;
    font-size: 17px;
    letter-spacing: 1px;
    line-height: 1.35;
    opacity: .9;
  }

  /* Back */
  .card-back { background: var(--paper); color: var(--ink); }
  .back-brand {
    position: absolute;
    right: 40px;
    top: 40px;
    width: 250px;
    color: var(--navy);
  }
  .back-brand .brand-name { font-size: 22px; letter-spacing: 1.5px; }
  .back-brand .brand-name .brand-sub { font-size: 15px; letter-spacing: 2px; }
  .back-brand .brand-rule { background: var(--rule); height: 2px; margin-top: 6px; }

  .person {
    position: absolute;
    left: 38px;
    right: 40px;
    top: 184px;
  }
  .person-name { color: var(--navy); font-weight: 700; font-size: 17px; }
  .person-title {
    display: flex;
    align-items: center;
    gap: 12px;
    font-size: 17px;
    margin-bottom: 12px;
  }
  .person-title::after { content: ""; flex: 1; height: 1px; background: var(--rule); }
  .contact-list { list-style: none; font-size: 17px; line-height: 1.35; }
  .contact-list li { display: flex; align-items: center; gap: 8px; }
  .contact-list .gap { margin-top: 8px; }
  .contact-list small { font-size: 11px; }
  .icon { width: 14px; height: 14px; fill: var(--navy); flex: none; }

  .offices {
    position: absolute;
    right: 40px;
    top: 242px;
    text-align: right;
    font-size: 16px;
    line-height: 1.3;
  }
  .offices address { font-style: normal; margin-bottom: 10px; }
</style>
</head>
<body>

<section class="card card-front">
  <div class="front-brand">
    <div class="brand-name">Hartwell<span class="brand-sub">Financial Advisory</span></div>
    <div class="brand-rule"></div>
  </div>
  <p class="disclaimer">Investment advisory services offered through Summit Ridge<br>Capital Partners, LLC, an SEC Registered Investment Advisor</p>
</section>

<section class="card card-back">
  <div class="back-brand">
    <div class="brand-name">Hartwell<span class="brand-sub">Financial Advisory</span></div>
    <div class="brand-rule"></div>
  </div>

  <div class="person">
    <p class="person-name">Daniel Marsh</p>
    <p class="person-title">Financial Advisor</p>
    <ul class="contact-list">
      <li><svg class="icon" viewBox="0 0 16 16"><circle cx="8" cy="8" r="7.5" fill="none" stroke="#13317a" stroke-width="1.2"/><path d="M5 4.5c.6-.4 1.2-.3 1.5.3l.6 1.2c.2.4 0 .8-.3 1l-.4.3c.4.9 1.1 1.6 2 2l.3-.4c.2-.3.6-.5 1-.3l1.2.6c.6.3.7.9.3 1.5-.6.8-1.6 1-2.6.5C6.3 10.1 5 8.8 4.4 6.6 4.1 5.7 4.3 5 5 4.5z"/></svg>817 555 0142 <small>(Fort Worth)</small></li>
      <li><svg class="icon" viewBox="0 0 16 16"><circle cx="8" cy="8" r="7.5" fill="none" stroke="#13317a" stroke-width="1.2"/><path d="M5 4.5c.6-.4 1.2-.3 1.5.3l.6 1.2c.2.4 0 .8-.3 1l-.4.3c.4.9 1.1 1.6 2 2l.3-.4c.2-.3.6-.5 1-.3l1.2.6c.6.3.7.9.3 1.5-.6.8-1.6 1-2.6.5C6.3 10.1 5 8.8 4.4 6.6 4.1 5.7 4.3 5 5 4.5z"/></svg>972 555 0187 <small>(Plano)</small></li>
      <li class="gap"><svg class="icon" viewBox="0 0 16 16"><path d="M1 4h14v9H1z"/><path d="M1 4l7 5 7-5" fill="none" stroke="#f7f7f7" stroke-width="1.2"/></svg>daniel@hartwellfa.com</li>
      <li><svg class="icon" viewBox="0 0 16 16"><circle cx="8" cy="8" r="7"/><path d="M1 8h14M8 1c-3 3-3 11 0 14M8 1c3 3 3 11 0 14M2.5 4.5h11M2.5 11.5h11" fill="none" stroke="#f7f7f7" stroke-width="1"/></svg>www.hartwellfa.com</li>
    </ul>
  </div>

  <div class="offices">
    <address>2200 Meadow Ln, Suite 300<br>Fort Worth, Texas 76110</address>
    <address>450 Cedar Ridge Dr, Suite 210<br>Plano, Texas 75075</address>
  </div>
</section>

</body>
</html>
```